Training company needs a Quick Reference Card design

We have draft skeleton of the design and most of the text. But we need a designer to take it the rest if the way.
I have designed a 2 page quick reference card - it is meant to be a 2-sided document. The first page is portrait, the back page can either be portrait or landscape, I'm not too concerned, whichever fits best.
Section called 'Maps' on front, a map is a collection of documents (like a manual), a topic is a document (like a page or section of a manual) and a block is a section of a document. The graphic is mean to illustrate the hierarchy but essentially a map is a big document with smaller documents in it.
Please use the company's logo colors to differentiate the different sections with minimal/ highlight only use of the darkest color, preferably.
Please use the icons for the corresponding Information types in the chart of the back - except please re-design the icons color scheme to match the company's logo/website colors.

Target Market(s)

Technical writers, after attending our training course, as an ongoing resource for them

Industry/Entity Type

It Company

Font styles to use
Sans Serif

Requirements
Must have
• Must adhere to look and feel of brand/ website. www.lumenrivet.com
Nice to have
• Please keep the design modern and slick looking, not too busy, easy to read

```html
<!DOCTYPE html>
<html lang="en">
<head>
<meta charset="utf-8">
<title>Quick Reference Card</title>
<link href="https://fonts.googleapis.com/css2?family=Oswald:wght@500;600;700&family=Source+Sans+3:wght@400;600;700&display=swap" rel="stylesheet">
<style>
:root{
  --indigo:#1e1aa8;
  --cyan:#17a3dc;
  --blue:#2453d9;
  --ink:#222;
  --slate:#4a4a4a;
  --line:#9a9a9a;
  --cell:#efefef;
  --bg:#e7e4df;
  --paper:#fff;
}
*{margin:0;padding:0;box-sizing:border-box}
html,body{width:1200px;height:1200px;overflow:hidden;background:var(--bg)}
body{position:relative;font-family:"Source Sans 3",sans-serif;color:var(--ink)}
.card{position:absolute;top:228px;width:718px;height:925px;background:var(--paper);transform:scale(.8);transform-origin:0 0;box-shadow:0 2px 6px rgba(0,0,0,.18);overflow:hidden}
.card.front{left:17px}
.card.back{left:609px}
.abs{position:absolute}
.brand{left:30px;top:38px;display:flex;align-items:center;gap:12px}
.brand-dot{width:64px;height:64px;border-radius:50%;background:var(--indigo)}
.brand-name{font-family:"Source Sans 3",sans-serif;font-weight:700;font-size:26px;line-height:1;color:var(--indigo);letter-spacing:.5px}
.title{left:320px;top:50px;font-family:"Oswald",sans-serif;font-weight:600;font-size:35px;letter-spacing:.3px;color:var(--cyan);white-space:nowrap}
.title .lead{color:var(--indigo)}
/* map */
.map{left:29px;top:137px;width:257px;height:169px;border:1.5px solid var(--line)}
.map h2{font-family:"Oswald",sans-serif;font-weight:500;font-size:30px;color:var(--indigo);text-align:center;margin-top:4px;line-height:1.1}
.map-col{position:absolute;top:50px;width:82px;text-align:center}
.map-col h3{font-family:"Source Sans 3",sans-serif;font-weight:400;font-size:15px;margin-bottom:4px}
.pill{background:var(--cyan);color:#fff;font-size:11.5px;padding:2px 0;border:1.5px solid #7fd0ef}
.pill.sub{margin-top:30px}
.map-rule{position:absolute;left:128px;top:58px;width:1px;height:82px;background:#bbb}
/* banners */
.banner{left:322px;width:396px;height:52px;color:#fff;font-size:11.5px;line-height:1.25;padding:9px 50px 0 10px}
.banner b{font-size:14px;font-weight:600}
.banner svg{position:absolute;right:0;top:0}
.banner.dark{background:var(--indigo)}
.banner.light{background:var(--cyan)}
/* section heads */
.section-head{display:flex;align-items:center;gap:9px;font-family:"Oswald",sans-serif;font-weight:600;font-size:17px;color:var(--cyan)}
.section-icon{width:30px;height:30px;border-radius:50%;background:var(--indigo);display:flex;align-items:center;justify-content:center}
/* rule boxes */
.rule{border:1.5px solid var(--line);padding:5px;text-align:center}
.rule h4{font-family:"Oswald",sans-serif;font-weight:500;font-size:11px;color:#fff;padding:8px 0;margin-bottom:8px}
.rule h4.c{background:var(--cyan)}
.rule h4.d{background:var(--indigo)}
.rule p{font-size:11.5px;line-height:1.2;padding:0 6px}
.note{background:var(--slate);border:2px solid #888;color:#fff;padding:6px 10px;font-size:11px}
.note h5{font-family:"Source Sans 3",sans-serif;font-weight:400;font-size:13.5px;margin-bottom:4px}
.note li{list-style:none;display:flex;align-items:center;gap:6px;line-height:1.45}
.num{width:9px;height:9px;border-radius:50%;background:var(--cyan);font-size:6px;display:inline-flex;align-items:center;justify-content:center}
.dot{width:5px;height:5px;border-radius:50%;background:var(--cyan)}
/* footer */
.contact{left:30px;top:848px;width:658px;height:45px;display:flex;align-items:center;justify-content:space-between;padding:0 10px 0 14px;color:#fff;font-size:12px;font-weight:600}
.contact.blue{background:linear-gradient(90deg,#1b3fc7,var(--blue))}
.contact.cyan{background:var(--cyan)}
.contact span{display:flex;align-items:center;gap:9px}
.contact .phone{font-size:14px;font-weight:400}
.base{left:0;top:910px;width:718px;height:15px;background:#555}
/* table */
.grid{left:30px;top:153px;width:658px;height:647px;border-collapse:collapse;table-layout:fixed}
.grid td,.grid th{border:1.5px solid #5a5a5a;text-align:center;vertical-align:middle;font-size:11.5px;line-height:1.2;padding:2px 3px;font-weight:400}
.grid thead th{background:var(--indigo);color:#fff;font-family:"Oswald",sans-serif;font-weight:500;font-size:12.5px;height:36px}
.grid thead th.corner{background:#fff}
.grid tbody th{background:var(--cyan);color:#fff;font-family:"Oswald",sans-serif;font-weight:600;font-size:13px;line-height:1.25}
.grid td.g{background:var(--cell)}
</style>
</head>
<body>

<section class="card front">
  <div class="abs brand"><div class="brand-dot"></div><div class="brand-name">LUMEN<br>RIVET</div></div>
  <h1 class="abs title"><span class="lead">QUICK</span> REFERENCE CARD</h1>

  <div class="abs map">
    <h2>MAP</h2>
    <div class="map-col" style="left:31px"><h3>TOPIC</h3><div class="pill">Primary Block</div><div class="pill sub">Sub-Block</div></div>
    <div class="map-rule"></div>
    <div class="map-col" style="left:142px"><h3>TOPIC</h3><div class="pill">Primary Block</div><div class="pill sub">Sub-Block</div></div>
  </div>

  <div class="abs banner dark" style="top:136px"><b>A map</b> is a file that organizes topics into structured collections of information. Maps specify hierarchy and relationships among topics.
    <svg width="30" height="52"><polygon points="0,0 30,10 30,52 0,52" fill="#14127c"/></svg></div>
  <div class="abs banner light" style="top:196px"><b>A topic</b> is a group of related blocks with a title. Use the chunking principle to group together relevant blocks.
    <svg width="30" height="52"><polygon points="0,0 30,0 30,44 0,52" fill="#0f82b4"/></svg></div>
  <div class="abs banner dark" style="top:253px;height:55px"><b>A block</b> is a bite-sized chunk of information about one main idea that allows the writer to organize the material into logical sections.
    <svg width="30" height="55"><polygon points="0,0 30,10 30,55 0,55" fill="#14127c"/></svg></div>

  <div class="abs section-head" style="left:247px;top:320px"><div class="section-icon"><svg width="16" height="16" viewBox="0 0 16 16"><path d="M3 13 L4 9 L11 2 L14 5 L7 12 Z" fill="#fff"/></svg></div>GENERAL WRITING RULES</div>

  <div class="abs rule" style="left:30px;top:363px;width:169px;height:148px"><h4 class="c">EFFECTIVE SENTENCES</h4><p>One main agent, action &amp; outcome. Use active voice and simplest tense possible. No more than 7 sentences per paragraph. Use lists and tables.</p></div>
  <div class="abs rule" style="left:266px;top:363px;width:170px;height:148px"><h4 class="d">SPECIAL CHARACTERS</h4><p>Avoid special characters, spell out words instead. Remove parentheses, colons and dashes. Avoid using quotation marks and slashes.</p></div>
  <div class="abs rule" style="left:518px;top:363px;width:170px;height:148px"><h4 class="c">PLAIN LANGUAGE</h4><p>Write in short sentences. Provide useful titles. Use clear familiar words. Avoid excess words. Be consistent.</p></div>

  <div class="abs note" style="left:32px;top:549px;width:310px;height:84px">
    <h5>3 Questions to ask before you start writing:</h5>
    <ul><li><span class="num">1</span>What is the purpose of this information?</li><li><span class="num">2</span>What is the desired user response of this information?</li><li><span class="num">3</span>Who is the audience?</li></ul>
  </div>
  <div class="abs note" style="left:386px;top:549px;width:302px;height:84px;padding:12px 26px">
    <h5>2 Types of language arts:</h5>
    <ul><li><span class="dot"></span>LAFI – Language arts for information</li><li><span class="dot"></span>LAFPR – language arts for personal response</li></ul>
  </div>

  <div class="abs section-head" style="left:249px;top:652px"><div class="section-icon"><svg width="16" height="16" viewBox="0 0 16 16"><circle cx="8" cy="8" r="6" fill="none" stroke="#fff" stroke-width="1.5"/><path d="M5 8 L7.2 10.2 L11 5.8" fill="none" stroke="#fff" stroke-width="1.8"/></svg></div>4 COGNITIVE PRINCIPLES</div>

  <div class="abs rule" style="left:31px;top:697px;width:141px;height:127px"><h4 class="c">CONSISTENCY</h4><p>Use similar terms and structures. Pick a term and stick with it. Use the same sequence of blocks. Use consistent styles.</p></div>
  <div class="abs rule" style="left:201px;top:697px;width:142px;height:127px"><h4 class="d">CHUNKING</h4><p>Maximum of nine (7 +/- 2) items in a list, rows in a table, blocks in a topic, or topics in a map.</p></div>
  <div class="abs rule" style="left:372px;top:697px;width:142px;height:127px"><h4 class="c">RELEVANCE</h4><p>Group similar items together. Separate relevance? Separate block. Irrelevant? Delete it.</p></div>
  <div class="abs rule" style="left:546px;top:697px;width:142px;height:127px"><h4 class="d">TITLING</h4><p>Name everything. Name every block, every topic, every map and every table column.</p></div>

  <div class="abs contact blue">
    <span class="phone"><svg width="20" height="20" viewBox="0 0 20 20"><circle cx="10" cy="10" r="8.5" fill="none" stroke="#fff" stroke-width="1.4"/><path d="M7 5.5 L9 8 L8 9 Q9 11.5 11 12 L12 11 L14.5 13 L13 14.5 Q8 14 5.5 8 Z" fill="#fff"/></svg>+1 (555) 010-4420</span>
    <span><svg width="20" height="14" viewBox="0 0 20 14"><rect x="1" y="1" width="18" height="12" fill="none" stroke="#fff" stroke-width="1.4"/><path d="M1 1 L10 8 L19 1" fill="none" stroke="#fff" stroke-width="1.4"/></svg>more-info@lumenrivet.com</span>
    <span><svg width="19" height="19" viewBox="0 0 20 20" fill="none" stroke="#fff" stroke-width="1.3"><circle cx="10" cy="10" r="8.5"/><ellipse cx="10" cy="10" rx="3.8" ry="8.5"/><path d="M1.5 10 H18.5 M3 5.5 H17 M3 14.5 H17"/></svg>www.lumenrivet.com</span>
  </div>
  <div class="abs base"></div>
</section>

<section class="card back">
  <div class="abs brand"><div class="brand-dot"></div><div class="brand-name">LUMEN<br>RIVET</div></div>
  <h1 class="abs title"><span class="lead">QUICK</span> REFERENCE CARD</h1>

  <table class="abs grid">
    <colgroup><col style="width:84px"><col style="width:109px"><col style="width:109px"><col style="width:113px"><col style="width:121px"><col style="width:122px"></colgroup>
    <thead><tr><th class="corner"></th><th>DEFINITION</th><th>CONCEPT</th><th>PRINCIPLE</th><th>PROCESS</th><th>TASK</th></tr></thead>
    <tbody>
      <tr style="height:70px"><th>DEFINITION</th><td class="g">Describes things the reader needs to know</td><td>Explains things the reader needs to understand</td><td class="g">Advises the reader what they need to do or not do and when</td><td>Demonstrates to the reader how things work</td><td class="g">Instructs the reader on how to do things</td></tr>
      <tr style="height:121px"><th>TYPES OF AUTHORING MODELS</th><td class="g">Sentences/phrases<br>Lists (ol, ul)<br>Tables<br>Diagrams<br>Part-description<br>Part-function</td><td>Sentences<br>/phrases<br>Lists (ol, ul)<br>Tables<br>Illustrations</td><td class="g">Sentences<br>/phrases<br>Lists (ol, ul)<br>Tables<br>Decision tree<br>Graphic</td><td>Sentences<br>/phrases<br>Stage<br>ordered list<br>When/then<br>condition tree<br>Graphic example</td><td class="g">Sentences<br>/phrases<br>Lists<br>If/then<br>decision tree<br>Graphic example</td></tr>
      <tr style="height:160px"><th>TITLING BEST PRACTICES</th><td class="g">Describes the item and anything that differentiates it from other items</td><td>Use the plural form of the noun, if one exists. Don't add additional words such as “About”, “What is”, or “Definition”</td><td class="g">Identifies the principle and expresses the gravity of the principle. Formula= gravity + principle, or principle + gravity</td><td>Human processes: Gerund of verb + noun “Grooming a dog”. System processes: Use “How (item) works” Ex “How engines work”</td><td class="g">Starts with an imperative verb, do not use gerund. “Mow the lawn” “Boil and egg” “Register for a course”</td></tr>
      <tr style="height:68px"><th>PRIMARY BLOCK TITLE</th><td class="g">Introduction</td><td>Definition</td><td class="g">Statement</td><td>Summary</td><td class="g">Purpose</td></tr>
      <tr style="height:107px"><th>PRIMARY BLOCK CONTENT</th><td class="g">Provide a description of the reference topic and how it would be used</td><td>Provide the exact meaning of the concept</td><td class="g">Provide a high-level summary of the principle</td><td>Provide a short explanation of the purpose of the process, or the need for the process</td><td class="g">Provide an explanation of why or when the reader would use the task</td></tr>
      <tr><th>TIPS AND EXAMPLES</th><td class="g"></td><td></td><td class="g"></td><td></td><td class="g"></td></tr>
    </tbody>
  </table>

  <div class="abs contact cyan">
    <span class="phone"><svg width="20" height="20" viewBox="0 0 20 20"><circle cx="10" cy="10" r="8.5" fill="none" stroke="#fff" stroke-width="1.4"/><path d="M7 5.5 L9 8 L8 9 Q9 11.5 11 12 L12 11 L14.5 13 L13 14.5 Q8 14 5.5 8 Z" fill="#fff"/></svg>+1 (555) 010-4420</span>
    <span><svg width="20" height="14" viewBox="0 0 20 14"><rect x="1" y="1" width="18" height="12" fill="none" stroke="#fff" stroke-width="1.4"/><path d="M1 1 L10 8 L19 1" fill="none" stroke="#fff" stroke-width="1.4"/></svg>more-info@lumenrivet.com</span>
    <span><svg width="19" height="19" viewBox="0 0 20 20" fill="none" stroke="#fff" stroke-width="1.3"><circle cx="10" cy="10" r="8.5"/><ellipse cx="10" cy="10" rx="3.8" ry="8.5"/><path d="M1.5 10 H18.5 M3 5.5 H17 M3 14.5 H17"/></svg>www.lumenrivet.com</span>
  </div>
  <div class="abs base"></div>
</section>

</body>
</html>
```